Website Design For Stitchcraftparlour.com

What: A range of Tapestry Kits, books & Accessories.
Who: Appeals to ladies 45-70 years.

What we need:
A home page and template for a product page
The home page needs to include the image and something we can use as a logo to get started.

Image:
I love the 'Maud Pellingham' feel, hearts, flags and bunting.
Tapestry tends to be rich, heavy fabrics so dark burgendy reds and navy blues might work quite well in moderation.

Layout:
I would like the core structure of the site to be similar to:
http://www.fernyplumes.co.uk (although this is just a suggestion feel free to try something else if you think it might work better.
Buttons along the top: Home, About Tapestry, Delivery, Contact Us (the drop down on Our Range is Tapestry Cushions.

I would also like the search box to be a little bigger and can be relocated.

Tabs under the image
Cushion Kits, Hanging Tapestrys, Books, Accessories, Advice
Then an area for featured products under that.

Images - You can use any of the images from The Vintage Linenwork Company - tapestry section to build a feel for how the site might look when populated with product.

Female 45-75yrs -

• Build with SEO in mind.
Some space for text on home page for seo
Some images below to give a feel for styling

```html
<!DOCTYPE html>
<html lang="en">
<head>
<meta charset="utf-8">
<title>The Stitchcraft Parlour – Cushion Kits</title>
<link rel="stylesheet" href="https://fonts.googleapis.com/css2?family=Arimo:ital,wght@0,400;0,700;1,400;1,700&family=Poiret+One&display=swap">
<style>
:root{
  --navy:#1d3a6c;
  --navy-dark:#142a52;
  --link:#1f3f78;
  --red:#b8161c;
  --red-dark:#8c1016;
  --red-light:#d8353a;
  --blue-tab:#6f98c6;
  --blue-tab-light:#9dbbdc;
  --green:#5fa91b;
  --green-light:#8fd043;
  --line:#d8d8d8;
  --frame:#c9c9c9;
  --text:#222;
  --nav-top:#d3dde8;
  --nav-bottom:#a6b9cd;
  --white:#fff;
}
*{box-sizing:border-box;margin:0;padding:0}
html,body{width:1117px;height:1200px;overflow:hidden;background:var(--white)}
body{font-family:Arimo,Arial,sans-serif;color:var(--text)}
a{color:inherit;text-decoration:none}
.stage{position:absolute;left:0;top:0;width:1024px;height:1100px;transform:scale(1.0908);transform-origin:0 0}

/* header */
.brand{position:absolute;left:40px;top:80px;display:flex;align-items:center;gap:12px}
.brand__mark{width:18px;height:18px;background:var(--red)}
.brand__name{font-family:'Poiret One',Arial,sans-serif;font-size:33px;color:var(--navy);font-weight:400;letter-spacing:.5px}
.brand__tagline{position:absolute;left:118px;top:136px;font-size:12px;font-style:italic;font-weight:700;color:var(--navy)}

.search{position:absolute;left:519px;top:28px;display:flex;gap:4px}
.search__field{width:235px;height:23px;border:1px solid #9a9a9a;box-shadow:inset 0 1px 3px rgba(0,0,0,.25);font-size:14px;color:#999;padding:3px 9px}
.search__button{width:25px;height:22px;background:var(--red-dark);display:flex;align-items:center;justify-content:center}
.account-links{position:absolute;left:817px;top:35px;font-size:11px;color:var(--link);display:flex;align-items:center}
.account-links .sep{width:2px;height:17px;background:var(--navy);margin:0 8px}
.header-rule{position:absolute;left:475px;top:63px;width:508px;height:4px;background:var(--line)}
.service-bar{position:absolute;left:580px;top:70px;width:403px;height:54px;background:linear-gradient(var(--red-light),var(--red));box-shadow:0 1px 3px rgba(0,0,0,.35);color:var(--white);font-size:12px;font-style:italic}
.service-bar__item{position:absolute;top:20px;display:flex;align-items:center;gap:12px}
.service-bar__divider{position:absolute;left:193px;top:4px;height:44px;border-left:2px dashed var(--white)}
.service-bar__rule{position:absolute;left:7px;right:7px;top:42px;height:1px;background:var(--white)}

/* main frame */
.page{position:absolute;left:33px;top:162px;width:950px;height:926px;border:1px solid var(--frame);box-shadow:0 1px 4px rgba(0,0,0,.2);background:var(--white)}
.main-nav{height:36px;background:linear-gradient(var(--nav-top),var(--nav-bottom));display:flex;justify-content:flex-end;gap:22px;padding:12px 48px 0 0;font-size:12.5px;color:var(--navy)}

/* sidebar */
.side-heading{position:absolute;left:18px;width:141px;height:27px;background:var(--navy);color:var(--white);font-size:12px;padding:6px 0 0 8px;clip-path:polygon(0 0,100% 0,88% 50%,100% 100%,0 100%)}
.side-box{position:absolute;left:18px;width:171px;border:2px solid #dcdcdc;border-top:none;border-radius:0 0 4px 4px}
.category-list{list-style:none;padding:8px 3px}
.category-list li{height:31px;margin-bottom:3.5px;color:var(--white);font-size:15px;padding:6px 0 0 12px;box-shadow:0 1px 2px rgba(0,0,0,.4)}
.category-list .tab-red{background:linear-gradient(var(--red-light),var(--red-dark))}
.category-list .tab-blue{background:linear-gradient(var(--blue-tab-light),var(--blue-tab))}
.theme-list{list-style:none;padding:14px 0 0 16px}
.theme-list li{font-size:15px;color:var(--link);text-decoration:underline;height:32px}

/* content */
.content{position:absolute;left:218px;top:56px;width:700px}
.content h1{font-size:17px;font-weight:400;color:#2b4a80;margin-left:1px}
.intro{font-size:10px;line-height:15px;margin:16px 0 0 4px;width:690px}
.product-grid{position:absolute;left:-4px;top:97px;display:grid;grid-template-columns:repeat(4,169px);column-gap:9px;row-gap:25px}
.product{height:195px;border:1px solid var(--frame);text-align:center;position:relative}
.product__image{display:block;width:116px;height:101px;margin:14px auto 0}
.product__name{font-size:9.5px;margin-top:19px}
.product__price{font-size:9.5px;margin-top:12px}
.product__button{display:inline-block;margin-top:3px;width:74px;height:18px;border-radius:9px;background:linear-gradient(var(--green-light),var(--green));color:var(--white);font-size:9.5px;font-weight:700;line-height:18px}

/* footer */
.footer-rule{position:absolute;left:21px;top:797px;width:904px;height:4px;background:var(--line)}
.footer{position:absolute;left:25px;top:822px;width:895px;font-size:9.5px;display:flex;align-items:center}
.footer__legal{margin-left:27px}
.footer__legal a{margin-right:14px}
.payments{margin-left:auto;display:flex;align-items:center;gap:3px}
.payments__label{font-size:10.5px;font-weight:700;font-style:italic;color:var(--navy);margin-right:6px}
.payment{width:29px;height:20px;border:1px solid #888;font-size:6px;font-weight:700;display:flex;align-items:center;justify-content:center;color:var(--white)}
</style>
</head>
<body>
<div class="stage">

<header>
  <div class="brand"><span class="brand__mark"></span><span class="brand__name">The Stitchcraft Parlour</span></div>
  <p class="brand__tagline">the best tapestry in the world</p>

  <form class="search">
    <div class="search__field">Search here</div>
    <div class="search__button">
      <svg width="16" height="14" viewBox="0 0 16 14" aria-hidden="true"><circle cx="5.5" cy="5.5" r="3.8" fill="none" stroke="#fff" stroke-width="2"/><line x1="8.5" y1="8" x2="14" y2="12.5" stroke="#fff" stroke-width="2.6" stroke-linecap="round"/></svg>
    </div>
  </form>
  <nav class="account-links"><a href="#">View Basket</a><span class="sep"></span><a href="#">My Account</a></nav>
  <div class="header-rule"></div>

  <div class="service-bar">
    <div class="service-bar__item" style="left:22px">
      <svg width="32" height="16" viewBox="0 0 32 16" aria-hidden="true"><rect x="0" y="1" width="19" height="10" fill="#fff"/><path d="M20 4h7l4 4v4H20z" fill="#fff"/><circle cx="6" cy="13" r="2.6" fill="#fff" stroke="#b8161c"/><circle cx="25" cy="13" r="2.6" fill="#fff" stroke="#b8161c"/></svg>
      <span>Fast &amp; Free Delivery</span>
    </div>
    <div class="service-bar__divider"></div>
    <div class="service-bar__item" style="left:209px">
      <svg width="34" height="22" viewBox="0 0 34 22" aria-hidden="true" style="margin-top:-6px"><rect x="1" y="1" width="30" height="19" fill="none" stroke="#fff" stroke-width="1.5" transform="rotate(-6 16 11)"/><path d="M2 3l15 9 14-11" fill="none" stroke="#fff" stroke-width="1.5"/></svg>
      <span>Need help? email us!</span>
    </div>
    <div class="service-bar__rule"></div>
  </div>
</header>

<div class="page">
  <nav class="main-nav">
    <a href="#">Home</a><a href="#">About Tapestry</a><a href="#">Our Range</a><a href="#">Delivery</a><a href="#">Contact Us</a>
  </nav>

  <aside>
    <div class="side-heading" style="top:52px">Shop by Categories</div>
    <div class="side-box" style="top:79px;height:189px">
      <ul class="category-list">
        <li class="tab-red">Cushion Kits</li>
        <li class="tab-blue">Hanging Tapestrys</li>
        <li class="tab-red">Books</li>
        <li class="tab-blue">Accessories</li>
        <li class="tab-red">Advice</li>
      </ul>
    </div>
    <div class="side-heading" style="top:276px">Shop by Theme</div>
    <div class="side-box" style="top:303px;height:221px">
      <ul class="theme-list">
        <li>Alphabet</li><li>Animal</li><li>Baby</li><li>Cupcakes</li><li>Holidays</li><li>Seaside</li>
      </ul>
    </div>
  </aside>

  <main class="content">
    <h1>Cushion Kits</h1>
    <p class="intro">The Stitchcraft Parlour is your online destinations for the best tapestry! We have all that you need! Lorem ipsum dolor sit amet, consectetur adipiscing elit. Fusce sed mi at arcu tristique posuere eu nec orci. Sed ut erat mollis sem ultrices hendrerit. Vivamus id mauris at nisl aliquet lacinia imperdiet at neque. Donec eleifend arcu at libero suscipit sollicitudin.</p>

    <div class="product-grid">
      <article class="product"><div class="product__image" role="img" aria-label="Photo of a rectangular union flag tapestry cushion" style="background:linear-gradient(135deg,#e8e2d6,#3f5a86 45%,#a33a40 70%,#e6e0d4)"></div><p class="product__name">Union Jack Rectangular Cushion</p><p class="product__price">£45.00</p><a class="product__button" href="#">View Now</a></article>
      <article class="product"><div class="product__image" role="img" aria-label="Photo of a heart shaped union flag cushion on a sofa" style="background:linear-gradient(135deg,#7a2a2c,#b9b6b8 40%,#8a3b44 65%,#5a4a40)"></div><p class="product__name">Union Jack Heart Cushion</p><p class="product__price">£45.00</p><a class="product__button" href="#">View Now</a></article>
      <article class="product"><div class="product__image" role="img" aria-label="Photo of a sampler cushion beside a toy rabbit on a chair" style="background:linear-gradient(135deg,#c9a77c,#e5d8c4 45%,#cdb79a 75%,#a47c56)"></div><p class="product__name">Union Jack Rectangular Cushion</p><p class="product__price">£45.00</p><a class="product__button" href="#">View Now</a></article>
      <article class="product"><div class="product__image" role="img" aria-label="Photo of a pink cushion stitched with rows of cupcakes" style="background:linear-gradient(135deg,#e8c7c9,#f1d9dc 45%,#d9a4b1 75%,#c9b8a8)"></div><p class="product__name">Cupcake Madness</p><p class="product__price">£45.00</p><a class="product__button" href="#">View Now</a></article>

      <article class="product"><div class="product__image" role="img" aria-label="Photo of a keep calm union flag cushion with pompom trim" style="background:linear-gradient(135deg,#8a6f55,#9fb0c8 40%,#c7a54a 60%,#a3404a 80%)"></div><p class="product__name">Keep Calm and Carry On</p><p class="product__price">£45.00</p><a class="product__button" href="#">View Now</a></article>
      <article class="product"><div class="product__image" role="img" aria-label="Photo of a striped cushion stitched with the word love" style="background:linear-gradient(135deg,#d8cfc4,#e9e3da 45%,#b55a4e 70%,#ddd4c8)"></div><p class="product__name">Love Cushion</p><p class="product__price">£45.00</p><a class="product__button" href="#">View Now</a></article>
      <article class="product"><div class="product__image" role="img" aria-label="Photo of a London landmarks sampler cushion" style="background:linear-gradient(135deg,#6b4a3a,#dde2ea 40%,#b4bfd3 65%,#7a5a48)"></div><p class="product__name">London</p><p class="product__price">£45.00</p><a class="product__button" href="#">View Now</a></article>
      <article class="product"><div class="product__image" role="img" aria-label="Photo of an owl cushion with pompom trim" style="background:linear-gradient(135deg,#6a4a34,#d9dcdf 40%,#b8873c 65%,#5e4332)"></div><p class="product__name">Twit Twoo Cushion</p><p class="product__price">£45.00</p><a class="product__button" href="#">View Now</a></article>
    </div>
  </main>

  <div class="footer-rule"></div>
  <footer class="footer">
    <span>© 2012 The Stitchcraft Parlour</span>
    <nav class="footer__legal"><a href="#">Terms and Conditions</a><a href="#">Privacy Policy</a></nav>
    <div class="payments">
      <span class="payments__label">PAYMENT OPTIONS</span>
      <span class="payment" style="background:#1d3a6c">Cardwise</span>
      <span class="payment" style="background:#1d3a6c">Paymora</span>
      <span class="payment" style="background:#1d3a6c">Amberline</span>
      <span class="payment" style="background:#1d3a6c">Pocketpay</span>
      <span class="payment" style="background:#c9411a">Bank</span>
    </div>
  </footer>
</div>

</div>
</body>
</html>
```